Flyer for Custom Home Builder!

my company is Harlow Ridge Homes, I am looking for a flyer that we can send via email to a customer, or print and hand out. I am thinking four pages so we could print this and fold it., possibly creating a folder. The name of the company is Harlow Ridge Homes our website is here www.harlowridgehomes-example.com. Some text you can use "Crafting luxury homes isn't just a job, it's our passion.
With meticulous attention to detail and an unwavering commitment to using the finest materials, Harlow Ridge Homes consistently delivers exceptional results that stand as a testament to our commitment to quality."

"Trust is the cornerstone of our foundation.
With a proven track record of delivering on our promises for over 16 years, we prioritize transparent communication and integrity throughout every step of the home-building journey".

you may need to obtain the photos here
https://files.example-share.net/f/k27pw4m8zrt03xq61bnv/h?key=48vn2c9q1x7mb5t0ekd3h&dl=0

Target Market(s)

We build homes for every wealthy clients, therefore the photos are extremely important

Industry/Entity Type

Construction.

Requirements
Must have
• clear larger photos

```html
<!DOCTYPE html>
<html lang="en">
<head>
<meta charset="utf-8">
<title>Harlow Ridge Homes – Folded Flyer</title>
<link href="https://fonts.googleapis.com/css2?family=Montserrat:wght@300;400;600&display=swap" rel="stylesheet">
<style>
  :root {
    --bg: #e4e2de;
    --ink: #0c0c0c;
    --paper-text: #f2f2f2;
    --sky-top: #8fb0cc;
    --sky-low: #d6dce0;
    --warm: #c0925c;
    --water: #6fa3ad;
    --wood: #a57a52;
  }
  * { box-sizing: border-box; margin: 0; padding: 0; }
  html, body { width: 1200px; height: 900px; overflow: hidden; }
  body {
    background: var(--bg);
    font-family: "Montserrat", sans-serif;
    display: flex; align-items: center; justify-content: center;
  }
  .flyer {
    width: 1120px; height: 780px;
    display: grid; grid-template-columns: 540px 580px;
    background: var(--ink);
    box-shadow: 0 10px 30px rgba(0,0,0,.18);
  }
  .photo { display: block; }

  /* Left page */
  .page-left { display: grid; grid-template-rows: 610px 170px; }
  .hero {
    background:
      radial-gradient(ellipse 40% 30% at 30% 78%, rgba(232,176,104,.85), transparent 70%),
      linear-gradient(180deg, var(--sky-top) 0%, var(--sky-low) 48%, #8a8782 62%, #4a4641 78%, #1e1d1b 100%);
  }
  .band {
    position: relative; color: var(--paper-text);
    display: flex; flex-direction: column; align-items: center; padding-top: 24px;
  }
  .brand-name {
    font-weight: 600; letter-spacing: .16em; text-transform: uppercase;
    color: var(--paper-text); font-size: 20px; line-height: 1.2; text-align: center;
  }
  .contact-row {
    position: absolute; left: 26px; right: 26px; bottom: 22px;
    display: flex; justify-content: space-between;
  }
  .contact { font-size: 9px; font-weight: 300; color: var(--paper-text); }
  .contact li { list-style: none; display: flex; align-items: center; gap: 6px; margin-top: 5px; text-decoration: underline; white-space: nowrap; }
  .contact svg { width: 9px; height: 9px; fill: var(--paper-text); flex: none; }

  /* Right page */
  .page-right { display: grid; grid-template-columns: 310px 270px; }
  .photo-stack { display: grid; grid-template-rows: 380px 400px; }
  .pool {
    background:
      radial-gradient(ellipse 55% 35% at 60% 75%, rgba(111,163,173,.95), transparent 70%),
      linear-gradient(165deg, #d8dadb 0%, #b8b6b2 18%, var(--wood) 32%, #2a2e30 52%, #4f7f88 72%, #c9d0d2 100%);
  }
  .kitchen {
    background:
      radial-gradient(ellipse 30% 20% at 45% 40%, rgba(236,180,110,.8), transparent 70%),
      linear-gradient(160deg, #3a3632 0%, #e8e4dd 22%, #d2c6b6 50%, var(--warm) 75%, #2f2b27 100%);
  }
  .side {
    padding: 30px 22px 24px; color: var(--paper-text);
    display: flex; flex-direction: column; align-items: center;
  }
  .side .brand-name { font-size: 17px; }
  .tagline { font-size: 10px; font-weight: 300; text-align: center; margin-top: 10px; line-height: 1.5; }
  .stairs {
    width: 226px; height: 250px; margin-top: 22px;
    background: linear-gradient(135deg, #2c2823 0%, var(--wood) 35%, #e6dccd 62%, #c39a6e 80%, #4d4034 100%);
  }
  .body-copy { font-size: 9.5px; font-weight: 300; line-height: 1.7; text-align: center; margin-top: 30px; }
  .side .contact { align-self: flex-start; margin-top: auto; font-size: 8.5px; }
</style>
</head>
<body>
  <main class="flyer">
    <section class="page-left">
      <div class="photo hero" role="img" aria-label="Modern white luxury home at dusk with glass walls reflected in an infinity pool"></div>
      <footer class="band">
        <p class="brand-name">Harlow Ridge<br>Homes</p>
        <div class="contact-row">
          <ul class="contact">
            <li><svg viewBox="0 0 10 10"><path d="M2 0h2l1 3-1.5 1a6 6 0 0 0 2.5 2.5L7 5l3 1v2c0 1-1 2-2 2A8 8 0 0 1 0 2c0-1 1-2 2-2z"/></svg>555-014-2286</li>
            <li><svg viewBox="0 0 10 10"><path d="M0 2h10v6H0zM0 2l5 3.5L10 2" stroke="#0c0c0c" stroke-width=".8"/></svg>info@harlowridgehomes-example.com</li>
          </ul>
          <ul class="contact">
            <li><svg viewBox="0 0 10 10"><path d="M2 0h2l1 3-1.5 1a6 6 0 0 0 2.5 2.5L7 5l3 1v2c0 1-1 2-2 2A8 8 0 0 1 0 2c0-1 1-2 2-2z"/></svg>555-014-2286</li>
            <li><svg viewBox="0 0 10 10"><path d="M0 2h10v6H0zM0 2l5 3.5L10 2" stroke="#0c0c0c" stroke-width=".8"/></svg>www.harlowridgehomes-example.com</li>
          </ul>
        </div>
      </footer>
    </section>

    <section class="page-right">
      <div class="photo-stack">
        <div class="photo pool" role="img" aria-label="Poolside terrace of a modern home with wood soffit and glass doors"></div>
        <div class="photo kitchen" role="img" aria-label="Bright open-plan kitchen and living area with pendant lights"></div>
      </div>
      <aside class="side">
        <p class="brand-name">Harlow Ridge<br>Homes</p>
        <p class="tagline">Crafting luxury homes isn't just a job,<br>it's our passion.</p>
        <div class="photo stairs" role="img" aria-label="Floating wooden staircase with glass railing"></div>
        <p class="body-copy">With meticulous attention to detail and an unwavering commitment to using the finest materials, Harlow Ridge Homes consistently delivers exceptional results that stand as a testament to our commitment to quality.</p>
        <ul class="contact">
          <li><svg viewBox="0 0 10 10"><path d="M2 0h2l1 3-1.5 1a6 6 0 0 0 2.5 2.5L7 5l3 1v2c0 1-1 2-2 2A8 8 0 0 1 0 2c0-1 1-2 2-2z"/></svg>555-014-2286</li>
          <li><svg viewBox="0 0 10 10"><path d="M0 2h10v6H0zM0 2l5 3.5L10 2" stroke="#0c0c0c" stroke-width=".8"/></svg>info@harlowridgehomes-example.com</li>
        </ul>
      </aside>
    </section>
  </main>
</body>
</html>
```